Innovative Consulting Firm Needs New Business Cards and Stationary

Our Innovative Consulting Firm, Harrowgate Consulting, is in need of new business cards and stationary designs. We want two-sided cards that incorporate our logo, which is attached. We are looking for something not too formal, but is professional and slick.

Card should have the following information:
Name (ex. Lena Vork)
Title (ex. Manager)
Address (ex. 24680 Quill Avenue)
Address 2 (ex. Suite 100)
City
State
Zip Code
Mobile
Email

The card should also have our website: www.harrowgateconsulting.example

Industry/Entity Type

Management Consulting

Contact Information for Business Card

Name (ex. Lena Vork)
Title (ex. Manager)
Address 2 (ex. Suite 100)
City
State
Zip Code
Mobile
Email

Font styles to use
Sans Serif

Requirements
Must have
• The colors on the card must match the colors in the logo. The exact color codes are attached in a pdf.
Nice to have
• The Company's Tagline is "Focused on your Future". This might be nice to incorporate, but not necessary.

```html
<!DOCTYPE html>
<html lang="en">
<head>
<meta charset="utf-8">
<title>Harrowgate Consulting — Business Cards</title>
<link rel="stylesheet" href="https://fonts.googleapis.com/css2?family=Lato:wght@400;700&display=swap">
<style>
  :root {
    --navy: #234c7a;
    --orange: #f0ab2a;
    --white: #ffffff;
    --stage: #e6e7ea;
    --ink: #234c7a;
  }
  * { margin: 0; padding: 0; box-sizing: border-box; }
  html, body {
    width: 1200px; height: 810px; overflow: hidden;
    background: var(--stage);
    font-family: "Lato", Arial, sans-serif;
  }
  .canvas { position: relative; width: 1200px; height: 810px; }

  .card {
    position: absolute;
    width: 560px; height: 320px;
    border-radius: 18px;
    overflow: hidden;
    background: var(--white);
    box-shadow: 0 10px 28px rgba(0,0,0,.18);
  }
  .card--front { left: 70px; top: 70px; }
  .card--back  { left: 570px; top: 420px; }

  .brand {
    position: absolute;
    display: flex; align-items: center; gap: 10px;
    color: var(--ink);
    font-weight: 700;
    white-space: nowrap;
  }
  .brand__dot {
    width: 16px; height: 16px; border-radius: 50%;
    background: var(--orange); flex: none;
  }
  .card--front .brand { left: 92px; top: 118px; font-size: 30px; }

  .front-band {
    position: absolute; left: 0; right: 0; bottom: 0;
    height: 40px; background: var(--navy);
    display: flex; align-items: center; justify-content: center;
    color: var(--white); font-size: 14px; font-weight: 700;
    letter-spacing: 2px;
  }

  .back-shape { position: absolute; inset: 0; }
  .card--back .brand { left: 24px; top: 172px; font-size: 19px; gap: 8px; }
  .card--back .brand__dot { width: 14px; height: 14px; }

  .details {
    position: absolute; right: 24px; top: 26px;
    text-align: right; color: var(--white);
    white-space: nowrap;
  }
  .details__name { font-size: 19px; letter-spacing: .5px; text-transform: uppercase; }
  .details__title { font-size: 11px; margin-top: 2px; }
  .details__address { font-size: 13px; line-height: 1.3; margin-top: 52px; }
  .details__contact { list-style: none; font-size: 12px; line-height: 1.5; margin-top: 20px; }
  .details__contact li { display: flex; justify-content: flex-end; align-items: center; gap: 6px; }
  .icon { width: 10px; height: 10px; fill: var(--white); flex: none; }
</style>
</head>
<body>
<main class="canvas">

  <section class="card card--front" aria-label="Card front">
    <div class="brand"><span class="brand__dot"></span>Harrowgate Consulting</div>
    <div class="front-band">www.harrowgateconsulting.example</div>
  </section>

  <section class="card card--back" aria-label="Card back">
    <svg class="back-shape" viewBox="0 0 560 320" width="560" height="320" aria-hidden="true">
      <path d="M160,0 C262,26 276,160 280,320 L560,320 L560,0 Z" fill="var(--orange)"/>
      <path d="M178,0 C274,24 292,160 298,320 L560,320 L560,0 Z" fill="var(--navy)" stroke="var(--white)" stroke-width="2"/>
    </svg>

    <div class="brand"><span class="brand__dot"></span>Harrowgate Consulting</div>

    <div class="details">
      <p class="details__name">Lena Vork</p>
      <p class="details__title">Manager</p>
      <p class="details__address">24680 Quill Avenue<br>Suite 100, City, State<br>Zip Code 1005</p>
      <ul class="details__contact">
        <li>(000) 0000 000
          <svg class="icon" viewBox="0 0 24 24"><path d="M6.6 10.8a15 15 0 0 0 6.6 6.6l2.2-2.2a1 1 0 0 1 1-.25 11.4 11.4 0 0 0 3.6.57 1 1 0 0 1 1 1V20a1 1 0 0 1-1 1A17 17 0 0 1 3 4a1 1 0 0 1 1-1h3.5a1 1 0 0 1 1 1c0 1.25.2 2.45.57 3.57a1 1 0 0 1-.25 1z"/></svg>
        </li>
        <li>info@harrowgateconsulting.example
          <svg class="icon" viewBox="0 0 24 24"><path d="M2 5h20v14H2z M4 7l8 6 8-6" fill="none" stroke="#fff" stroke-width="2"/></svg>
        </li>
        <li>www.harrowgateconsulting.example
          <svg class="icon" viewBox="0 0 24 24"><circle cx="12" cy="12" r="9" fill="none" stroke="#fff" stroke-width="2"/><path d="M3 12h18M12 3c3 3 3 15 0 18M12 3c-3 3-3 15 0 18" fill="none" stroke="#fff" stroke-width="1.6"/></svg>
        </li>
      </ul>
    </div>
  </section>

</main>
</body>
</html>
```